Forget what you know about corporate well

I need a one-page flies used for print, to embedding in a website, all social media platforms and email.

Target Market(s)

Business

Industry/Entity Type

Health And Wellness

Font styles to use
Serif
Script
Other font styles liked:
• I would like the designers opinion on the font

Colors

Designer to choose colors to be used in the design.

Requirements
Must have
• This is the wording:
• Did you know that 75% of healthcare costs are incurred by preventable diseases? Cardiovascular disease, cancer, and diabetes are the three major causes of rising health care plans and are all preventable.
• Milo and his team have spent decades learning how to increase productivity, reduce absenteeism, and increase employee engagement, all leading to lowering healthcare costs. Together, they have developed a system created to target the masses all while addressing individual needs. Their corporate training challenges helps to engrain positive habits through a carefully curated accountability and reward system.
• How it works:
• Step 1 – evaluate the needs of your business;
• Step 2 – set up individualized workshops based on highest needs;
• Step 3 – create a customized corporate training challenge.
• Why Milo?
• Milo excels at motivational speaking. He is an author, a nutritionist and a professional athlete with a master’s degree in clinical nutrition. He is a teacher of corporate wellness at Fernhollow College and a health coach. Milo has been featured in national magazines, podcasts, and popular fitness websites. Milo’s own health issues put him on a quest to heal himself and others. With twenty-five years of experience and a passion for wellness, he can provide your company with an unforgettable experience.
Nice to have
• I will not give my opinion, I believe that is an insult to the designer. All of the verbiage is above and I attached a plethora of pictures.
Should not have
• No opinion

```html
<!DOCTYPE html>
<html lang="en">
<head>
<meta charset="utf-8">
<title>Renewal Wellness – Milo T. Renner</title>
<link rel="stylesheet" href="https://fonts.googleapis.com/css2?family=Montserrat:wght@500&family=Roboto:ital,wght@0,400;1,500;1,700&family=Roboto+Condensed:wght@400;500&family=Libre+Baskerville:ital@1&display=swap">
<style>
:root{
  --lime:#b6d236;
  --lime-dark:#9cbc1e;
  --ink:#333333;
  --body:#4a4a4a;
  --banner:#2b2b2b;
  --chevron:#3d3d3d;
  --badge:#555555;
  --paper:#ffffff;
  --backdrop:#e9e9e7;
}
*{margin:0;padding:0;box-sizing:border-box}
html,body{width:1200px;height:1200px;overflow:hidden;background:var(--backdrop)}
.flyer{position:absolute;left:190px;top:20px;width:820px;height:1160px;background:var(--paper);overflow:hidden;font-family:"Roboto",sans-serif;color:var(--body)}
.brand{position:absolute;left:90px;top:62px;display:flex;align-items:center;gap:10px}
.brand-dot{width:18px;height:18px;border-radius:50%;background:var(--lime)}
.brand-name{font-family:"Roboto",sans-serif;font-weight:500;font-size:17px;color:var(--ink)}
.brand-owner{position:absolute;left:118px;top:92px;font-family:"Libre Baskerville",serif;font-style:italic;font-size:14px;color:var(--body)}
.rule{position:absolute;left:0;width:100%;height:6px;background:var(--lime)}
.rule-top{top:148px}
.rule-bottom{top:520px}
.banner{position:absolute;left:0;top:154px;width:100%;height:366px;background:linear-gradient(120deg,#3a3a3a 0%,#262626 55%,#303030 100%)}
.portrait{position:absolute;left:448px;top:22px;width:340px;height:498px;background:linear-gradient(180deg,#c9a08a 0%,#8a6a5c 30%,#2f4f73 55%,#24405f 100%);border-radius:150px 150px 0 0}
.quote{position:absolute;left:40px;top:296px;width:380px;text-align:center;font-family:"Montserrat",sans-serif;font-weight:500;font-size:19px;line-height:24px;color:#fff}
.quote-mark{position:absolute;font-family:"Montserrat",sans-serif;font-size:60px;line-height:1;color:var(--lime);font-weight:500}
.quote-open{left:36px;top:286px}
.quote-close{left:382px;top:348px}
.quote-source{position:absolute;left:230px;top:390px;font-family:"Libre Baskerville",serif;font-style:italic;font-size:15px;color:#fff}
.intro{position:absolute;left:70px;top:560px;width:680px}
.intro h2{font-style:italic;font-weight:500;font-size:17.5px;color:var(--lime-dark);margin-bottom:16px}
.intro p{font-size:12.5px;line-height:16px;color:var(--body)}
.steps{position:absolute;left:40px;top:748px;width:780px;height:160px;background:var(--lime)}
.chevron{position:absolute;top:0}
.step{position:absolute;top:0;width:220px;height:160px}
.step-badge{position:absolute;left:50%;top:-32px;margin-left:-34px;width:68px;height:68px;border-radius:50%;background:var(--badge);border:4px solid #fff;box-shadow:0 2px 5px rgba(0,0,0,.35);color:#fff;font-family:"Roboto Condensed",sans-serif;font-size:42px;line-height:60px;text-align:center}
.step-text{position:absolute;left:0;top:62px;width:100%;text-align:center;font-family:"Roboto Condensed",sans-serif;font-weight:500;font-size:18.5px;line-height:22px;color:var(--ink)}
.why{position:absolute;left:100px;top:930px;width:660px}
.why h2{font-style:italic;font-weight:500;font-size:17.5px;color:var(--lime-dark);margin-bottom:6px}
.why p{font-size:12px;line-height:15px;color:var(--body)}
.footer-rule{position:absolute;left:70px;top:1080px;width:680px;height:2px;background:#555}
.contacts{position:absolute;left:70px;top:1098px;width:680px;display:flex;justify-content:space-between;font-family:"Roboto Condensed",sans-serif;font-size:18px;color:var(--ink)}
.contact{display:flex;align-items:center;gap:8px}
.contact svg{width:16px;height:16px;fill:var(--lime-dark)}
</style>
</head>
<body>
<main class="flyer">
  <header>
    <div class="brand"><span class="brand-dot"></span><span class="brand-name">Renewal Wellness</span></div>
    <div class="brand-owner">Milo T. Renner</div>
  </header>

  <div class="rule rule-top"></div>
  <section class="banner" role="img" aria-label="Dimmed photo of Milo speaking to an audience on stage"></section>
  <div class="portrait" role="img" aria-label="Portrait of Milo smiling with arms crossed, wearing a striped blue sweater"></div>
  <span class="quote-mark quote-open">“</span>
  <blockquote class="quote">Milo is a brilliant motivational speaker. Your employees will become empowered!</blockquote>
  <span class="quote-mark quote-close">”</span>
  <cite class="quote-source">-Dr. Samir Haddad</cite>
  <div class="rule rule-bottom"></div>

  <section class="intro">
    <h2>Did you know that 75% of healthcare costs are incurred by preventable diseases?</h2>
    <p>Cardiovascular disease, cancer, and diabetes are the three major causes of rising health care plans and are all preventable.<br>
    Milo and his team have spent decades learning how to increase productivity, reduce absenteeism, and increase employee engagement, all leading to lowering healthcare costs. Together, they have developed a system created to target the masses all while addressing individual needs. Their corporate training challenges helps to engrain positive habits through a carefully curated accountability and reward system.</p>
  </section>

  <section class="steps">
    <svg class="chevron" style="left:205px" width="60" height="160" viewBox="0 0 60 160"><polygon points="0,0 24,0 60,80 24,160 0,160 36,80" fill="var(--chevron)"/></svg>
    <svg class="chevron" style="left:470px" width="60" height="160" viewBox="0 0 60 160"><polygon points="0,0 24,0 60,80 24,160 0,160 36,80" fill="var(--chevron)"/></svg>
    <div class="step" style="left:0"><div class="step-badge">1</div><div class="step-text">Evaluate the needs<br>of your business</div></div>
    <div class="step" style="left:255px"><div class="step-badge">2</div><div class="step-text">Set up individualized<br>workshops based on<br>highest needs</div></div>
    <div class="step" style="left:525px"><div class="step-badge">3</div><div class="step-text">Create a customized<br>corporate training<br>challenge</div></div>
  </section>

  <section class="why">
    <h2>Why Milo?</h2>
    <p>Milo excels at motivational speaking. He is an author, a nutritionist and a professional athlete with a master’s degree in clinical nutrition. He is a teacher of corporate wellness at Fernhollow College and a health coach. Milo has been featured in national magazines, podcasts, and popular fitness websites. Milo’s own health issues put him on a quest to heal himself and others. With twenty-five years of experience and a passion for wellness, he can provide your company with an unforgettable experience.</p>
  </section>

  <div class="footer-rule"></div>
  <footer class="contacts">
    <span class="contact"><svg viewBox="0 0 16 16"><path d="M3 1l3 3-1.5 2a9 9 0 0 0 5.5 5.5L12 10l3 3-2 2C6 15 1 10 1 3z"/></svg>(555) 014-2290</span>
    <span class="contact"><svg viewBox="0 0 16 16"><path d="M1 3h14v10H1z M2 4l6 5 6-5" stroke="#fff" stroke-width="1"/></svg>info@milorenner.com</span>
    <span class="contact"><svg viewBox="0 0 16 16"><circle cx="8" cy="8" r="7"/></svg>www.milorenner.com</span>
  </footer>
</main>
</body>
</html>
```